Brook Forge - Crypto Currency Miner Powered by Renewable Energy Website

We Need Web Pages Design for Website for Crypto Currency Miner

Serivices include:
Mining Rig Sales
Housing for Rigs turnkey on renewable energy grid
Cloud Mining term packages
Updates

http://www.vaultrigdigest.example (Competitors sites)

Target Market(s)

Investers for Mining Rigs and terms for 1,2 or 3 years of Hash rate

Industry/Entity Type

Mining

Number of Pages Required

5+ page

Font styles to use
Sans Serif

Colors
add136
9bcb3c
606060
474747
ffc214
cadf82
fbee3e
876aae
6b449b

Requirements
Must have
• Pictures of Solar, Wind and power Factor Correction units
Nice to have
• e-commerce platform so contract terms can be purchased through website
Should not have
• Heavy construction equipment

```html
<!DOCTYPE html>
<html lang="en">
<head>
<meta charset="utf-8">
<title>Brook Forge – Renewable Crypto Mining</title>
<link rel="stylesheet" href="https://fonts.googleapis.com/css2?family=Oswald:wght@400;500&family=Open+Sans:wght@400;600;700&display=swap">
<style>
:root{
  --green:#9bcb3c;
  --green-lite:#add136;
  --green-pale:#eaf3d6;
  --yellow:#ffc214;
  --grey:#606060;
  --dark:#474747;
  --darker:#3a3a3a;
  --white:#ffffff;
}
*{margin:0;padding:0;box-sizing:border-box}
html,body{width:1200px;height:4588px;overflow:hidden}
body{position:relative;font-family:"Open Sans",sans-serif;color:var(--grey);background:var(--white)}
.abs{position:absolute}
.heading{font-family:"Oswald",sans-serif;font-weight:400;text-transform:uppercase;line-height:1.05}
.btn{display:inline-block;font-family:"Oswald",sans-serif;font-size:20px;color:var(--white);background:var(--green);padding:8px 26px;text-transform:uppercase;letter-spacing:.5px}
.mark{display:inline-block;width:26px;height:26px;background:var(--green);margin-right:14px;vertical-align:middle}
.body-text{font-size:15px;line-height:1.55;color:var(--grey)}
.lead{font-size:17px;line-height:1.4;color:var(--green);font-weight:600}

/* hero */
.hero{left:0;top:0;width:1200px;height:760px;background:linear-gradient(180deg,#f3a800 0%,#f6b91a 35%,#c98410 70%,#2b1f0a 100%)}
.nav{left:0;top:0;width:1200px;height:96px;background:rgba(30,22,8,.55)}
.brand{left:150px;top:28px;font-family:"Open Sans",sans-serif;font-weight:700;font-size:28px;color:var(--white)}
.brand-dot{display:inline-block;width:34px;height:34px;border-radius:50%;background:var(--white);vertical-align:middle;margin-right:10px}
.menu{left:455px;top:38px;display:flex;gap:34px;font-family:"Oswald",sans-serif;font-size:17px;color:var(--white);text-transform:uppercase;letter-spacing:.5px}
.hero-title{left:790px;top:130px;color:var(--white);font-size:66px}
.hero-btn{left:920px;top:390px;background:#2a2a2a;font-size:22px}
.hero-coin{left:730px;top:440px;width:280px;height:280px;border-radius:50%;background:radial-gradient(circle at 40% 35%,#ffe27a,#e2a61a 60%,#9a6a0c)}

/* features */
.features{left:0;top:760px;width:1200px;height:420px}
.feature{top:100px;width:300px;text-align:center;color:#5a4400}
.feature svg{display:block;margin:0 auto 18px}
.feature h3{font-family:"Oswald",sans-serif;font-weight:400;font-size:22px;text-transform:uppercase;line-height:1.2;margin-bottom:12px}
.feature p{font-size:12px;line-height:1.5}

/* buy */
.buy-title{left:150px;top:1390px;font-family:"Oswald",sans-serif;font-size:48px;color:var(--green)}
.buy-lead{left:200px;top:1470px;width:360px}
.buy-text{left:200px;top:1545px;width:380px;font-size:12px}
.buy-btn{left:465px;top:1615px}
.phone{left:745px;top:1220px;width:262px;height:775px;border-radius:42px;background:var(--white);border:3px solid #cfcfcf;box-shadow:0 4px 18px rgba(0,0,0,.18);z-index:3}
.phone-screen{position:absolute;left:14px;top:86px;width:228px;height:540px;background:linear-gradient(160deg,#9bcb3c,#2f9a3a);display:flex;flex-direction:column;align-items:center;justify-content:center;color:var(--white);font-weight:700;font-size:24px}
.phone-screen span{display:block;width:56px;height:56px;border-radius:50%;background:var(--white);margin-bottom:12px}
.phone-speaker{position:absolute;left:101px;top:42px;width:54px;height:6px;border-radius:3px;background:#cfcfcf}
.phone-home{position:absolute;left:100px;top:660px;width:56px;height:56px;border-radius:50%;border:3px solid #cfcfcf}

/* why */
.why{left:0;top:1940px;width:1200px;height:680px;background:var(--green-pale)}
.step-label{font-family:"Oswald",sans-serif;font-size:17px;color:var(--green)}
.why-title{left:700px;top:100px;font-size:52px;color:var(--green)}
.why-text{left:720px;top:232px;width:360px;font-size:12px}
.why-btn{left:890px;top:585px}

/* about */
.about{left:0;top:2620px;width:1200px;height:740px;background:linear-gradient(180deg,#6b86a4 0%,#c9a07a 45%,#e7b26a 60%,#5b6b38 80%,#3c4a26 100%)}
.about-title{left:180px;top:430px;font-family:"Oswald",sans-serif;font-size:52px;color:var(--white)}
.about-lead{left:220px;top:510px;width:340px;color:#e9f7c7}
.about-text{left:220px;top:575px;width:370px;font-size:12px;color:#f1f1f1}
.about-btn{left:220px;top:645px}

/* consult */
.coin-big{left:-90px;top:3380px;width:560px;height:600px;border-radius:50%;background:radial-gradient(circle at 45% 40%,#ffe690,#e0a523 55%,#8f620d)}
.consult-title{left:570px;top:3580px;font-size:46px;color:var(--green)}
.consult-lead{left:612px;top:3705px;width:400px}
.consult-text{left:612px;top:3775px;width:400px;font-size:12px}
.consult-btn{left:900px;top:3850px}

/* footer */
.footer{left:0;top:4140px;width:1200px;height:400px;background:var(--dark);color:#d8d8d8}
.footer h4{font-family:"Oswald",sans-serif;font-weight:400;font-size:28px;color:var(--white);margin-bottom:14px}
.footer li{list-style:none;font-size:14px;line-height:1.7}
.post{display:flex;gap:14px;margin-bottom:18px}
.post i{flex:none;width:54px;height:54px;background:var(--yellow)}
.post p{font-size:13px;line-height:1.4}
.legal{left:0;top:4540px;width:1200px;height:48px;font-size:11px;color:#777}
.social{display:flex;gap:8px}
.social i{width:22px;height:22px;border-radius:50%;background:#3b7fc4}
</style>
</head>
<body>

<header class="hero abs" role="img" aria-label="Wind turbines silhouetted against a golden sunset sky"></header>
<div class="hero-coin abs" role="img" aria-label="Gold crypto coin"></div>
<nav class="nav abs">
  <div class="brand abs"><span class="brand-dot"></span>Brook Forge</div>
  <div class="menu abs"><span>Home</span><span>Pricing</span><span>Our Offer</span><span>About Us</span><span>Customer Service</span></div>
</nav>
<h1 class="hero-title heading abs">Start<br>Brook Forge<br>Today!</h1>
<a class="hero-btn btn abs">Start Now!</a>

<section class="features abs">
  <svg class="abs" style="left:0;top:0" width="1200" height="420" viewBox="0 0 1200 420"><polygon points="0,0 1200,0 1200,420 0,250" fill="#ffc214"/></svg>
  <div class="feature abs" style="left:150px">
    <svg width="64" height="64" viewBox="0 0 64 64" fill="none" stroke="#5a4400" stroke-width="2.5"><circle cx="32" cy="24" r="4"/><path d="M32 20V4M35 26l14 8M29 26l-14 8M32 28v32M24 60h16"/></svg>
    <h3>Wind Power<br>Investment</h3>
    <p>Invest in turbine hash power and earn steady daily returns from clean mining farms run on wind.</p>
  </div>
  <div class="feature abs" style="left:450px">
    <svg width="64" height="64" viewBox="0 0 64 64" fill="none" stroke="#5a4400" stroke-width="2.5"><path d="M12 12h40l6 30H6z M9 27h46 M24 12l-3 30 M40 12l3 30 M32 42v12 M22 56h20"/></svg>
    <h3>Solar Power<br>Investment</h3>
    <p>Invest in solar hash power and earn steady daily returns from clean mining farms run on sunlight.</p>
  </div>
  <div class="feature abs" style="left:750px">
    <svg width="64" height="64" viewBox="0 0 64 64" fill="none" stroke="#5a4400" stroke-width="2.5"><rect x="8" y="18" width="48" height="36" rx="4"/><path d="M14 18l28-10 4 10 M40 32h16v10H40z"/></svg>
    <h3>Get Your First<br>Payout Today</h3>
    <p>Start a plan today and get your first payout sent straight to your wallet within hours.</p>
  </div>
</section>

<h2 class="buy-title abs"><span class="mark"></span>Buy And Sell Bitcoin</h2>
<p class="buy-lead lead abs">Buy and sell coins in seconds with low fees. Safe trades, instant settlement, full control.</p>
<p class="buy-text body-text abs">Trade from your account at any hour with clear prices and no hidden charges. Funds move between your wallet and your mining balance with a single tap.</p>
<a class="buy-btn btn abs">Join Us</a>

<div class="phone abs">
  <div class="phone-speaker"></div>
  <div class="phone-screen"><span></span>Brook Forge</div>
  <div class="phone-home"></div>
</div>

<section class="why abs">
  <svg class="abs" style="left:130px;top:80px" width="450" height="520" viewBox="0 0 450 520" fill="none">
    <path d="M40 180h110M40 300h110M60 420h110M150 60h60" stroke="#9bcb3c" stroke-width="2"/>
    <g stroke-width="6">
      <polygon points="220,20 256,40 256,82 220,102 184,82 184,40" stroke="#2aa6df" fill="#fff"/>
      <polygon points="240,130 276,150 276,192 240,212 204,192 204,150" stroke="#2aa6df" fill="#fff"/>
      <polygon points="220,245 256,265 256,307 220,327 184,307 184,265" stroke="#ffc214" fill="#fff"/>
      <polygon points="240,360 276,380 276,422 240,442 204,422 204,380" stroke="#9bcb3c" fill="#fff"/>
    </g>
    <g font-family="Oswald,sans-serif" font-size="28" text-anchor="middle">
      <text x="220" y="72" fill="#2aa6df">A</text><text x="240" y="182" fill="#2aa6df">B</text>
      <text x="220" y="297" fill="#e6a800">C</text><text x="240" y="412" fill="#9bcb3c">D</text>
    </g>
    <g font-family="Oswald,sans-serif" font-size="15" fill="#606060">
      <text x="160" y="30">01</text><text x="282" y="140">02</text><text x="160" y="255">03</text><text x="282" y="370">04</text>
    </g>
    <g font-family="Oswald,sans-serif" font-size="17" fill="#9bcb3c">
      <text x="270" y="60">Safe And Secure</text><text x="40" y="172">Mobile App</text>
      <text x="270" y="290" fill="#e6a800">Secure Wallet</text><text x="20" y="412">Covered By Insurance</text>
    </g>
  </svg>
  <h2 class="why-title heading abs"><span class="mark"></span>Why Choose<br>Brook Forge?</h2>
  <div class="why-text body-text abs">
    <p style="margin-bottom:14px">Brook Forge offers you a smart and easy way to grow your money. Our mining system is made for people who are new to crypto as well as for seasoned experts and large investors. We run some of the largest farms powered by wind and sun, offering an easy way to take part in bitcoin mining without noise, heat or hardware at home.</p>
    <p>We are a team of experts in the digital currency sector, and our mining engine is designed to give the most efficient and reliable mining results.</p>
  </div>
  <a class="why-btn btn abs">More ...</a>
</section>

<section class="about abs" role="img" aria-label="Wind turbine in a green field at sunrise">
  <h2 class="about-title abs"><span class="mark"></span>About BROOK FORGE</h2>
  <p class="about-lead lead abs">We build clean mining farms on renewable grids. Powered by wind, run by people you trust.</p>
  <p class="about-text body-text abs">Our rigs are housed in turnkey sites on wind and solar energy, so every coin mined leaves a lighter footprint.</p>
  <a class="about-btn btn abs">Join Us</a>
</section>

<div class="coin-big abs" role="img" aria-label="Large gold crypto coin"></div>
<h2 class="consult-title heading abs"><span class="mark"></span>Are You Looking For<br><span style="padding-left:40px">A Consalting?</span></h2>
<p class="consult-lead lead abs">Talk to our mining advisers. We help you pick the right rig, term and hash rate plan.</p>
<p class="consult-text body-text abs">Book a free call to compare one, two and three year contracts and find the plan that suits your budget.</p>
<a class="consult-btn btn abs">More ...</a>

<footer class="footer abs">
  <div class="abs" style="left:150px;top:50px;width:260px">
    <div style="font-weight:700;font-size:24px;color:#fff;margin-bottom:16px"><span class="brand-dot" style="width:28px;height:28px"></span>Brook Forge</div>
    <p style="font-size:12px;line-height:1.6">Clean crypto mining for everyone. We run rigs on wind and solar power and share the returns with our members each day, with open reports and support.</p>
  </div>
  <div class="abs" style="left:470px;top:40px"><h4>Links</h4><ul><li>Home</li><li>About Us</li><li>Services</li><li>Our Offer</li><li>Contact Us</li></ul></div>
  <div class="abs" style="left:600px;top:40px;width:260px"><h4>Location</h4><ul>
    <li style="font-size:12px;line-height:1.5;margin-bottom:8px">Visit our main office or reach us by phone and email any day.</li>
    <li>48 Alder Lane, Fifth Avenue</li><li>(00) 555 010 200</li><li>(00) 555 010 201</li><li>hello@brookforge.example</li></ul></div>
  <div class="abs" style="left:870px;top:40px;width:220px"><h4>Popular Post</h4>
    <div class="post"><i></i><p>11 Things You Need to Know About Bitcoin – Sam Facts<br>Jan 14, 2018</p></div>
    <div class="post"><i></i><p>11 Things You Need to Know About Bitcoin – Sam Facts<br>Jan 14, 2018</p></div>
  </div>
</footer>
<div class="legal abs">
  <span class="abs" style="left:150px;top:16px">© Copyright 2018 Brook Forge. All Rights Reserved.</span>
  <div class="social abs" style="left:975px;top:4px"><i></i><i></i><i></i></div>
  <span class="abs" style="left:890px;top:30px">Privacy Policy | Partners | Sitemap</span>
</div>

</body>
</html>
```